Mortgage Loan officer needs clean/modern business card design

Looking for a clean, modern 2-sided business card design. We like the earth tones used in our logo and website http://vukarhome-lending.example . Would also like to incorporate: 1) Something special to make our card stand out - a pop of color or embossed logo, for instance and 2) please include "Mortgage Loans" "Reverse Mortgages" "Private Money Loans" on back of card with the logo.

Front: Needs to include agent/company license info - see website. Agent name: Niall Hargrove

Here are fonts and colors used for our logo:
Font: Avenir Next
Colors:
#2c3539 - Dark Gray
#576870 - Light Gray
#ffffff - Background White

Target Market(s)

Prospects and current clients. Will also be distributing to people in professional network (attorneys and CPAs)

Industry/Entity Type

Business

Contact Information for Business Card

Include agent name, contact info, website on front, licensing info for agent an company. Logo and services offered on back

Font styles to use
Other font styles liked:
• Avenir Next

Requirements
Must have
• See project description
Should not have
• Nothing cheesy

```html
<!DOCTYPE html>
<html lang="en">
<head>
<meta charset="utf-8">
<title>Vukar Home Lending – Business Card</title>
<link rel="stylesheet" href="https://fonts.googleapis.com/css2?family=Nunito+Sans:wght@400;600;700&display=swap">
<style>
  :root {
    --dark-gray: #2c3539;
    --light-gray: #576870;
    --card-white: #f2f2f2;
    --stage: #9b9b9b;
    --text-main: #2c3539;
    --text-soft: #576870;
    --back-text: #e6e8e9;
  }
  * { box-sizing: border-box; margin: 0; padding: 0; }
  html, body {
    width: 1105px; height: 1200px; overflow: hidden;
    background: var(--stage);
    font-family: "Nunito Sans", "Avenir Next", sans-serif;
  }
  .canvas { position: relative; width: 1105px; height: 1200px; }

  .card { position: absolute; left: 184px; width: 744px; height: 424px; overflow: hidden; }

  /* Front */
  .card-front { top: 120px; background: var(--card-white); }
  .agent-name {
    position: absolute; left: 46px; top: 54px;
    font-size: 25px; font-weight: 700; color: var(--text-main); letter-spacing: .5px;
  }
  .agent-title { position: absolute; left: 46px; top: 88px; font-size: 19px; color: var(--text-soft); }
  .address {
    position: absolute; left: 46px; top: 132px;
    font-size: 18px; line-height: 28px; color: var(--text-soft);
  }
  .contact-list {
    position: absolute; left: 46px; top: 226px; list-style: none;
    font-size: 18px; line-height: 28.6px; color: var(--text-main);
  }
  .contact-list li { display: flex; align-items: center; gap: 10px; }
  .contact-list svg { width: 17px; height: 17px; fill: var(--text-main); flex: none; }

  .brand-band {
    position: absolute; right: 0; top: 80px; width: 248px; height: 270px;
    background: var(--dark-gray);
  }
  .brand-seal {
    position: absolute; left: 400px; top: 133px; width: 192px; height: 192px;
    border-radius: 50%; background: var(--card-white);
    border: 1.5px solid var(--light-gray);
    display: flex; align-items: center; justify-content: center; text-align: center;
  }
  .brand-seal .brand-name {
    font-size: 25px; line-height: 31px; font-weight: 400; color: var(--light-gray);
  }

  /* Back */
  .card-back { top: 637px; background: var(--dark-gray); }
  .back-texture {
    position: absolute; inset: 0;
    background: radial-gradient(ellipse at 50% 45%, #323c40 0%, var(--dark-gray) 75%);
  }
  .back-brand {
    position: absolute; left: 0; right: 0; top: 120px; text-align: center;
    font-size: 56px; line-height: 66px; font-weight: 600; color: var(--back-text);
  }
  .services {
    position: absolute; left: 0; right: 0; top: 370px; text-align: center;
    font-size: 19px; color: var(--back-text);
  }
</style>
</head>
<body>
<main class="canvas">

  <section class="card card-front" aria-label="Card front">
    <h1 class="agent-name">NIALL HARGROVE</h1>
    <p class="agent-title">CEO/Founder</p>
    <p class="address">2190 Larkmoor Avenue, Suite 310<br>Fairhaven, CA 95030<br>Lic No :NMLS:604517</p>

    <ul class="contact-list">
      <li><svg viewBox="0 0 24 24"><path d="M6.6 10.8c1.4 2.8 3.8 5.1 6.6 6.6l2.2-2.2c.3-.3.7-.4 1-.2 1.1.4 2.3.6 3.6.6.6 0 1 .4 1 1V20c0 .6-.4 1-1 1C10.6 21 3 13.4 3 4c0-.6.4-1 1-1h3.5c.6 0 1 .4 1 1 0 1.3.2 2.5.6 3.6.1.3 0 .7-.2 1z"/></svg>555-310-4820 x138</li>
      <li><svg viewBox="0 0 24 24"><path d="M6.6 10.8c1.4 2.8 3.8 5.1 6.6 6.6l2.2-2.2c.3-.3.7-.4 1-.2 1.1.4 2.3.6 3.6.6.6 0 1 .4 1 1V20c0 .6-.4 1-1 1C10.6 21 3 13.4 3 4c0-.6.4-1 1-1h3.5c.6 0 1 .4 1 1 0 1.3.2 2.5.6 3.6.1.3 0 .7-.2 1z"/></svg>555-472-9160</li>
      <li><svg viewBox="0 0 24 24"><path d="M6 3h12v5H6zM3 9h18v8h-3v4H6v-4H3zm5 6v4h8v-4z"/></svg>555-310-4821</li>
      <li><svg viewBox="0 0 24 24"><path d="M2 5h20v14H2zm2 2v.5l8 5 8-5V7zm0 2.8V17h16V9.8l-8 5z"/></svg>vukarhome-lending.example</li>
      <li><svg viewBox="0 0 24 24"><path d="M12 2a10 10 0 1 0 0 20 10 10 0 0 0 0-20zm-1 17.9A8 8 0 0 1 4.2 9.8L9 14.6v1c0 1.1.9 2 2 2zm6.9-2.5c-.3-.8-1-1.4-1.9-1.4h-1v-3c0-.6-.4-1-1-1H8v-2h2c.6 0 1-.4 1-1V7h2c1.1 0 2-.9 2-2v-.4a8 8 0 0 1 2.9 12.8z"/></svg>www.vukarhome-lending.example</li>
    </ul>

    <div class="brand-band"></div>
    <div class="brand-seal">
      <span class="brand-name">Vukar Home<br>Lending</span>
    </div>
  </section>

  <section class="card card-back" aria-label="Card back">
    <div class="back-texture" role="img" aria-label="Subtle overlapping circle pattern on dark gray"></div>
    <p class="back-brand">Vukar Home<br>Lending</p>
    <p class="services">Mortgage Loans • Reverse Mortgages • Private Money Loans</p>
  </section>

</main>
</body>
</html>
```